Animal Hospital Business Cards

Make a business card look like the attached example

*Use the same blue/black coloring
*Brisket Hollow Animal Hospital (instead of pet home rounds)
*Emergency Services (instead of tamsin creek clinic)
*House Calls (instead of open 7 days by appointment)
*Change address to 278 Brisket Hollow Rd Loveland, OH 45263
*Open 7 days a week (instead of emergency service)
*Add the website www.briskethollowanimalhospital.example

On the back...
*instead of the text outlined in red, just white
*instead of the light blue, try your best to make it just like the blue and black on the front side of the card
*Delete "designed and printed by 9 whiskers inc, www.pressfeline.example

Requirements
Must have
• look just like the attached example with requested edits/changes

```html
<!DOCTYPE html>
<html lang="en">
<head>
<meta charset="utf-8">
<title>Brisket Hollow Animal Hospital – Business Cards</title>
<link href="https://fonts.googleapis.com/css2?family=Montserrat:wght@400;500;700&display=swap" rel="stylesheet">
<style>
  :root {
    --brand-blue: #435875;
    --ink: #111111;
    --paper: #ffffff;
    --mist: #e6e6e6;
    --backdrop: #3a3a3c;
  }
  * { box-sizing: border-box; margin: 0; padding: 0; }
  html, body { width: 1200px; height: 900px; overflow: hidden; }
  body {
    background: var(--backdrop);
    font-family: "Montserrat", sans-serif;
    color: var(--ink);
    position: relative;
  }
  .card {
    position: absolute;
    width: 630px;
    height: 360px;
    background: var(--paper);
    overflow: hidden;
    box-shadow: 0 6px 18px rgba(0,0,0,.35);
  }

  /* Appointment card (back) */
  .appointment-card { left: 470px; top: 50px; }
  .appointment-card .header-band {
    height: 96px;
    background: var(--brand-blue);
    color: var(--paper);
    text-align: center;
    padding-top: 16px;
    letter-spacing: 1.5px;
  }
  .header-band .card-title { font-size: 21px; font-weight: 500; }
  .header-band .doctor,
  .header-band .phone { font-size: 16px; line-height: 22px; }
  .appointment-form { padding: 44px 30px 0; font-size: 17px; letter-spacing: 1.5px; }
  .form-row { display: flex; align-items: flex-end; margin-bottom: 52px; white-space: nowrap; }
  .form-row:last-child { margin-bottom: 0; }
  .fill-line { flex: 1; border-bottom: 1px solid var(--ink); margin: 0 8px 4px; }
  .day-options { display: flex; justify-content: space-between; }
  .day { display: flex; align-items: center; gap: 5px; }
  .tick-box { width: 12px; height: 12px; border: 2px solid var(--ink); }
  .meridiem { font-size: 12px; line-height: 13px; }

  /* Business card (front) */
  .business-card { left: 110px; top: 470px; }
  .business-card .title-band {
    height: 78px;
    background: var(--brand-blue);
    color: var(--paper);
    text-align: center;
    padding-top: 12px;
  }
  .hospital-name { font-size: 28px; font-weight: 700; letter-spacing: .5px; }
  .hospital-tagline { font-size: 17px; letter-spacing: 6px; margin-top: 2px; }
  .service-band { height: 106px; background: var(--paper); position: relative; }
  .contact-band { height: 110px; background: var(--mist); position: relative; }
  .hours-band {
    height: 66px;
    background: var(--brand-blue);
    color: var(--paper);
    font-size: 23px;
    font-weight: 500;
    text-align: center;
    line-height: 66px;
  }
  .info-block {
    position: absolute;
    border-left: 2px solid var(--brand-blue);
    padding-left: 12px;
    font-size: 16px;
    line-height: 21px;
    white-space: nowrap;
  }
  .info-block .label { color: var(--brand-blue); font-weight: 700; font-size: 17px; }
  .service-emergency { left: 36px; top: 18px; }
  .service-housecalls { left: 262px; top: 40px; }
  .contact-address { left: 36px; top: 14px; }
  .contact-web { left: 262px; top: 40px; }
</style>
</head>
<body>

  <section class="card appointment-card">
    <header class="header-band">
      <div class="card-title">Veterinary Appointment</div>
      <div class="doctor">Marlow J. Pennick, DVM</div>
      <div class="phone">513.555.0147</div>
    </header>
    <div class="appointment-form">
      <div class="form-row">Your appointment for<span class="fill-line"></span>is on</div>
      <div class="form-row day-options">
        <span class="day"><span class="tick-box"></span>Mon.</span>
        <span class="day"><span class="tick-box"></span>Tues.</span>
        <span class="day"><span class="tick-box"></span>Wed.</span>
        <span class="day"><span class="tick-box"></span>Thurs.</span>
        <span class="day"><span class="tick-box"></span>Fri.</span>
        <span class="day"><span class="tick-box"></span>Sat.</span>
      </div>
      <div class="form-row">Date<span class="fill-line"></span>Time<span class="fill-line"></span><span class="meridiem">AM<br>PM</span></div>
    </div>
  </section>

  <section class="card business-card">
    <header class="title-band">
      <div class="hospital-name">Brisket Hollow Animal Hospital</div>
      <div class="hospital-tagline">(instead of pet home rounds)</div>
    </header>
    <div class="service-band">
      <div class="info-block service-emergency">
        <div class="label">Emergency Services</div>
        <div>instead of</div>
        <div>tamsin - creek - clinic</div>
      </div>
      <div class="info-block service-housecalls">
        <div class="label">House Calls</div>
        <div>instead of open 7 days</div>
        <div>By appointment</div>
      </div>
    </div>
    <div class="contact-band">
      <div class="info-block contact-address">
        <div>278 Brisket Hollow Rd</div>
        <div>Loveland, OH 45263</div>
      </div>
      <div class="info-block contact-web">
        <div>(523) 555 0147</div>
        <div>briskethollowanimalhospital.example</div>
      </div>
    </div>
    <footer class="hours-band">Open 7 days a week</footer>
  </section>

</body>
</html>
```